The Willow Hours - a modern wellness brand

Looking for a modern, simple, and clean website for a virtual consulting firm focused on holistic wellness and sustainable living. Want a strong combo of text and photos (really shitty starts are available for reference on www.thewillowhours.com and www.helenabrusco.com for reference - general idea is in the right direction, was too difficult to work through with the wordpress template and nothing laid out correctly)
Needs include:
- strong home / landing page
- ability to schedule (use calend.ly) on the site
- online shop / purchasing POS integration
- blog
-multiple 'services' pages
- about page
- contact page
(attached brand board images for brand style / reference)
Updates
Want more opportunity for designs and feedback
Target Market(s)
women and gay men aged 30-50
Coding
Coded - Design and coding required
Number of Pages Required
5+ page
Colors
Designer to choose only greyscale colors for use in the design.
Requirements
Must have
- the ability for me to update and manage through wordpress when things like pricing, or services change
Should not have
- complicated anything

```html
<!DOCTYPE html>
<html lang="en">
<head>
<meta charset="utf-8">
<title>The Willow Hours — Website Design</title>
<link rel="stylesheet" href="https://fonts.googleapis.com/css2?family=Cormorant+Garamond:wght@400;500;600&family=Jost:wght@300;400;500&display=swap">
<style>
:root{
  --ink:#000000;
  --night:#0b0b0b;
  --mist:#eeeeee;
  --paper:#f5f5f5;
  --panel:#f1f1f1;
  --backdrop:#e6e6e6;
  --white:#ffffff;
  --mute:#8c8c8c;
  --line:#d6d6d6;
  --serif:"Cormorant Garamond", "Times New Roman", serif;
  --sans:"Jost", "Helvetica Neue", Arial, sans-serif;
}
*{box-sizing:border-box;margin:0;padding:0}
html,body{width:1200px;height:3742px;overflow:hidden}
body{background:var(--backdrop);position:relative;font-family:var(--sans);color:var(--ink)}
.abs{position:absolute}

/* ---------- brand board ---------- */
.brand-mark{left:189px;top:104px;display:flex;align-items:center;gap:16px}
.brand-mark .dot{width:70px;height:70px;border:1.5px solid var(--ink);border-radius:50%;flex:none}
.brand-mark .name{font-family:var(--serif);font-weight:500;font-size:24px;letter-spacing:4px;line-height:1;white-space:nowrap}
.divider{width:1px;background:#c9c9c9;top:94px;height:88px}
.board-title{font-family:var(--sans);font-size:21px;font-weight:400}
.font-list{font-family:var(--serif);font-size:16px;line-height:26px;color:#333;white-space:nowrap}
.swatch{width:38px;height:38px;border-radius:50%;box-shadow:0 1px 3px rgba(0,0,0,.18)}
.swatch-label{font-size:8px;color:#666;width:50px;text-align:center}

/* ---------- desktop preview ---------- */
.preview{left:300px;top:292px;width:600px;height:380px;background:var(--white);box-shadow:0 6px 20px rgba(0,0,0,.12)}
.preview .pnav{height:30px;display:flex;align-items:center;justify-content:space-between;padding:0 16px}
.preview .pnav .pname{font-family:var(--serif);font-size:9px;letter-spacing:2px;font-weight:600}
.preview .pnav .plinks{display:flex;gap:10px;font-size:5px;letter-spacing:.5px;align-items:center}
.preview .pnav .pbtn{background:var(--ink);color:#fff;padding:4px 6px}
.preview .phero{position:absolute;left:10px;top:30px;width:580px;height:340px;background:linear-gradient(160deg,#f4f4f4 0%,#d9d9d9 45%,#bdbdbd 75%,#e2e2e2 100%)}
.preview .phead{position:absolute;left:120px;top:130px;font-family:var(--serif);font-size:24px;line-height:28px;color:#111}

/* ---------- page ---------- */
.page{left:293px;top:825px;width:613px;height:2825px;background:var(--white);overflow:hidden}
.nav{left:0;top:0;width:613px;height:46px}
.nav .logo{left:38px;top:13px;display:flex;align-items:center;gap:6px}
.nav .logo .dot{width:20px;height:20px;border:1px solid var(--ink);border-radius:50%}
.nav .logo .name{font-family:var(--serif);font-size:10px;font-weight:600;letter-spacing:2px;white-space:nowrap}
.nav .menu{left:259px;top:19px;display:flex;gap:13px;font-size:5.5px;letter-spacing:.5px;color:#555}
.nav .menu .active{color:var(--ink);border-bottom:1px solid var(--ink)}
.nav .cta{left:471px;top:14px;width:96px;height:18px;background:var(--ink);color:#fff;font-size:5.5px;letter-spacing:.5px;display:flex;align-items:center;justify-content:center}
.nav .cart{left:578px;top:17px}

.hero{left:10px;top:46px;width:593px;height:308px;background:radial-gradient(ellipse at 75% 10%,#ffffff 0%,#e9e9e9 25%,transparent 55%),linear-gradient(180deg,#d8d8d8 0%,#bdbdbd 45%,#cfcfcf 70%,#e8e8e8 100%)}
.display{font-family:var(--serif);font-weight:500;color:#111;white-space:nowrap}
.hero-line{font-size:25px;line-height:29px}
.underline{border-bottom:1.5px solid #111}

.side-label{font-size:5.5px;letter-spacing:1.5px;color:var(--mute);transform:rotate(-90deg);transform-origin:left top;white-space:nowrap}
.title{font-size:19px;line-height:22px}
.body-copy{font-size:6.2px;line-height:13.5px;color:#555}
.btn-outline{border:1px solid var(--ink);font-size:5.3px;letter-spacing:.5px;display:flex;align-items:center;justify-content:center;background:var(--white);white-space:nowrap}

.portrait-ring{left:313px;top:571px;width:116px;height:116px;border-radius:50%;border:2px dotted #222;padding:6px;background:var(--white);z-index:2}
.portrait{width:100%;height:100%;border-radius:50%;background:radial-gradient(circle at 50% 40%,#cfcfcf 0%,#8a8a8a 55%,#e2e2e2 100%)}

.process{left:0;top:628px;width:613px;height:337px;background:linear-gradient(115deg,#050505 0%,#1a1a1a 35%,#060606 55%,#161616 80%,#050505 100%);color:#fff}
.process .title{color:#fff}
.step-name{font-family:var(--serif);font-size:14px;color:#fff;white-space:nowrap}
.step-copy{font-size:5.2px;line-height:10px;color:#bdbdbd;width:87px}

.services{left:10px;top:1125px;width:593px;height:288px;background:var(--panel)}
.service-row{width:143px;height:32px;border-bottom:1px solid var(--line);display:flex;align-items:center;justify-content:space-between;font-size:9px;color:#a5a5a5}
.service-row.current{color:#222}

.product-card{width:103px}
.product-card .shot{width:103px;height:142px;background:linear-gradient(180deg,#f3f3f3,#e9e9e9)}
.product-card .ptitle{font-family:var(--serif);font-size:7px;text-align:center;margin-top:15px}
.product-card .price{font-size:7px;text-align:center;color:#666;margin-top:4px}
.product-card .add{margin:6px auto 0;width:61px;height:18px;border:1px solid var(--ink);font-size:5px;display:flex;align-items:center;justify-content:center}
.product-card .add.filled{background:var(--ink);color:#fff}

.appointment{left:0;top:1834px;width:613px;height:299px;background:radial-gradient(ellipse at 85% 30%,#2a2a2a 0%,#0a0a0a 45%,#000 100%);color:#fff}
.appointment .title{color:#fff}
.workspace{left:15px;top:2073px;width:231px;height:125px;background:linear-gradient(135deg,#f2f2f2 0%,#d0d0d0 60%,#e8e8e8 100%);z-index:2}

.quote-ring{left:108px;top:2256px;width:80px;height:80px;border-radius:50%;border:2px dotted #222;display:flex;align-items:center;justify-content:center;font-family:var(--serif);font-size:34px;font-weight:600}
.quote-text{left:219px;top:2262px;width:300px;font-family:var(--serif);font-size:11px;line-height:15px;color:#222}
.quote-source{font-family:var(--sans);font-size:6px;color:#777;margin-top:8px}

.news{left:10px;top:2387px;width:593px;height:369px;background:var(--panel)}
.post{left:111px;width:372px;height:77px;border:1px solid #e2e2e2;background:var(--panel)}
.post .thumb{position:absolute;left:10px;top:10px;width:113px;height:57px;background:linear-gradient(135deg,#e6e6e6,#bfbfbf)}
.post .date{position:absolute;left:133px;top:16px;font-size:4.5px;color:#888}
.post .ptitle{position:absolute;left:133px;top:25px;font-family:var(--serif);font-size:8.5px}
.post .more{position:absolute;left:133px;top:41px;font-size:4.5px;border-bottom:1px solid #333}

.footer-col{font-size:5.5px;line-height:10px;color:#333;white-space:nowrap}
.social{width:22px;height:22px;border-radius:50%;background:var(--ink)}
</style>
</head>
<body>

<!-- brand board -->
<div class="abs brand-mark">
  <div class="dot"></div>
  <div class="name">THE WILLOW HOURS</div>
</div>
<div class="abs divider" style="left:591px"></div>
<div class="abs board-title" style="left:647px;top:88px">Fonts:</div>
<div class="abs font-list" style="left:647px;top:128px">Larkspur Serif Medium<br>Fieldline Sans</div>
<div class="abs divider" style="left:850px"></div>
<div class="abs board-title" style="left:905px;top:88px">Colors:</div>
<div class="abs swatch" style="left:906px;top:123px;background:#000000"></div>
<div class="abs swatch" style="left:954px;top:123px;background:#eeeeee"></div>
<div class="abs swatch" style="left:1002px;top:123px;background:#f5f5f5"></div>
<div class="abs swatch-label" style="left:900px;top:168px">#000000</div>
<div class="abs swatch-label" style="left:948px;top:168px">#eeeeee</div>
<div class="abs swatch-label" style="left:996px;top:168px">#f5f5f5</div>

<!-- desktop hero preview -->
<div class="abs preview">
  <div class="pnav">
    <span class="pname">THE WILLOW HOURS</span>
    <span class="plinks"><span>HOME</span><span>ABOUT</span><span>SERVICES</span><span>BLOG</span><span>CONTACT</span><span>SHOP</span><span class="pbtn">SCHEDULE AN APPOINTMENT</span></span>
  </div>
  <div class="phero" role="img" aria-label="Soft black and white photo of a hand brushing through a sunlit meadow"></div>
  <div class="phead display">Resources and Support<br>&nbsp;for a strong<br>Mind, Body and Spirit</div>
</div>

<!-- full home page -->
<main class="abs page">
  <header class="abs nav">
    <div class="abs logo"><span class="dot"></span><span class="name">THE WILLOW HOURS</span></div>
    <nav class="abs menu"><span class="active">HOME</span><span>ABOUT</span><span>SERVICES</span><span>BLOG</span><span>CONTACT</span><span>SHOP</span></nav>
    <div class="abs cta">SCHEDULE AN APPOINTMENT</div>
    <svg class="abs cart" width="9" height="11" viewBox="0 0 9 11"><path d="M1 3h7v7H1z M3 3V2a1.5 1.5 0 0 1 3 0v1" fill="none" stroke="#333" stroke-width=".8"/></svg>
  </header>

  <section class="abs hero" role="img" aria-label="Soft black and white photo of a hand brushing through a sunlit meadow"></section>
  <div class="abs side-label" style="left:76px;top:255px">THE WILLOW HOURS</div>
  <h1 class="abs display hero-line" style="left:125px;top:146px;font-weight:500">Resources and Support</h1>
  <div class="abs display hero-line" style="left:110px;top:175px">for a strong</div>
  <div class="abs display hero-line" style="left:96px;top:204px"><span class="underline">Mind, Body and Spirit</span></div>
  <svg class="abs" style="left:98px;top:242px" width="14" height="14" viewBox="0 0 14 14"><path d="M12 2L2 12M2 5v7h7" fill="none" stroke="#111" stroke-width="1"/></svg>

  <!-- about -->
  <div class="abs side-label" style="left:76px;top:448px">ABOUT US</div>
  <h2 class="abs display title" style="left:132px;top:411px">The Willow</h2>
  <div class="abs display title" style="left:104px;top:433px">History</div>
  <p class="abs body-copy" style="left:224px;top:466px;width:182px">Over the last decade and a half, this site has grown along with me. Beginning as a blog in my early twenties, it chronicled my musings on life and growth. It was the first space I had to write, process and share how I was experiencing the world, good, bad, or otherwise, how the world was also experiencing me.</p>
  <div class="abs btn-outline" style="left:458px;top:565px;width:73px;height:18px">CONTINUE READING</div>

  <div class="abs portrait-ring"><div class="portrait" role="img" aria-label="Portrait photo of the founder"></div></div>

  <!-- process -->
  <section class="abs process">
    <div class="abs side-label" style="left:81px;top:100px;color:#777">HOW WE DO IT</div>
    <h2 class="abs display title" style="left:132px;top:57px">How We Work</h2>
    <div class="abs display title" style="left:104px;top:79px">The Process</div>

    <div class="abs step-name" style="left:81px;top:133px">1. Understand</div>
    <p class="abs step-copy" style="left:96px;top:153px;text-align:right">Always remember in the jungle there's a lot of them in there, after you overcome them, you will make it to paradise.</p>

    <div class="abs step-name" style="left:200px;top:159px">2. Imagine</div>
    <p class="abs step-copy" style="left:209px;top:180px;text-align:center">You see the hedges, how I got it shaped up? It's important to shape up your hedges, it's like getting a haircut, stay fresh.</p>

    <div class="abs step-name" style="left:317px;top:185px">3. Create</div>
    <p class="abs step-copy" style="left:327px;top:206px;text-align:center">We don't see them, we will never see them. To be successful you've got to work hard, to make history, simple, you've got to.</p>

    <div class="abs step-name" style="left:435px;top:210px">4. Build</div>
    <p class="abs step-copy" style="left:444px;top:231px;text-align:center">Look at the sunset. Surround yourself with angels, positive energy, beautiful people, beautiful souls, clean heart.</p>
  </section>

  <!-- contact prompt -->
  <div class="abs side-label" style="left:76px;top:1075px">GET IN TOUCH</div>
  <h2 class="abs display title" style="left:132px;top:1025px">Do You Think We</h2>
  <div class="abs display title" style="left:104px;top:1047px">Can Help You?</div>
  <div class="abs btn-outline" style="left:458px;top:1036px;width:73px;height:19px">CONTACT US NOW</div>

  <!-- services -->
  <section class="abs services">
    <div class="abs side-label" style="left:71px;top:74px">SERVICES</div>
    <h2 class="abs display title" style="left:122px;top:60px">What We</h2>
    <div class="abs display title" style="left:94px;top:82px">Offer You</div>
    <p class="abs body-copy" style="left:194px;top:112px;width:150px">Quis autem vel eum iure reprehenderit qui in ea voluptate velit esse quam nihil molestiae eum fugiat quo voluptas nulla pariatur.</p>
    <div class="abs service-row" style="left:378px;top:132px">Coaching<span>&rarr;</span></div>
    <div class="abs service-row current" style="left:378px;top:164px">Energy<span>&rarr;</span></div>
    <div class="abs service-row" style="left:378px;top:196px;border-bottom:none">Tarot<span>&rarr;</span></div>
  </section>

  <!-- products -->
  <div class="abs side-label" style="left:76px;top:1530px">MERCHANDISE</div>
  <h2 class="abs display title" style="left:132px;top:1473px">The Willow</h2>
  <div class="abs display title" style="left:104px;top:1495px">Products</div>
  <div class="abs product-card" style="left:83px;top:1536px">
    <div class="shot" role="img" aria-label="Hardcover book with a black and white cover"></div>
    <div class="ptitle">Product Title Goes Here</div><div class="price">$69.99</div><div class="add">ADD TO CART</div>
  </div>
  <div class="abs product-card" style="left:198px;top:1536px">
    <div class="shot" role="img" aria-label="Light book cover with birds in flight"></div>
    <div class="ptitle">Product Title Goes Here</div><div class="price">$79.99</div><div class="add filled">ADD TO CART</div>
  </div>
  <div class="abs product-card" style="left:313px;top:1536px">
    <div class="shot" role="img" aria-label="Book with a black mountain landscape cover"></div>
    <div class="ptitle">Product Title Goes Here</div><div class="price">$89.99</div><div class="add">ADD TO CART</div>
  </div>
  <div class="abs product-card" style="left:428px;top:1536px">
    <div class="shot" role="img" aria-label="White book with a large brace on the cover"></div>
    <div class="ptitle">Product Title Goes Here</div><div class="price">$99.99</div><div class="add">ADD TO CART</div>
  </div>
  <div class="abs" style="left:277px;top:1766px;font-size:5px;color:#555;border-bottom:1px solid #555">view all products</div>

  <!-- appointment -->
  <section class="abs appointment">
    <div class="abs side-label" style="left:81px;top:100px;color:#777">APPOINTMENT</div>
    <h2 class="abs display title" style="left:132px;top:58px">Get Started with The Willow Hours</h2>
    <div class="abs display title" style="left:104px;top:80px">Book Your Virtual Meeting Today</div>
    <p class="abs body-copy" style="left:312px;top:126px;width:222px;color:#bbb;font-size:5.6px;line-height:11px">Lorem ipsum dolor sit amet, consectetur adipiscing elit, sed do eiusmod tempor incididunt ut labore et dolore magna aliqua. Ut enim ad minim veniam, quis nostrud exercitation ullamco laboris nisi ut aliquip ex ea.</p>
    <p class="abs body-copy" style="left:312px;top:170px;width:222px;color:#bbb;font-size:5.6px;line-height:11px">Duis aute irure dolor in reprehenderit in voluptate velit esse cillum dolore eu fugiat nulla pariatur. Excepteur sint occaecat cupidatat non proident.</p>
    <div class="abs btn-outline" style="left:312px;top:225px;width:73px;height:18px;background:#000;color:#fff;border-color:#fff">GET STARTED TODAY</div>
  </section>
  <div class="abs workspace" role="img" aria-label="Overhead photo of hands typing on a laptop beside a plant and notebook"></div>

  <!-- quote -->
  <div class="abs quote-ring">&ldquo;</div>
  <blockquote class="abs quote-text">&ldquo;Doing the work to help ourselves to see and know our own worth, our power and our purpose enables us to see and know others more purposefully and fully as humans.&rdquo;
    <div class="quote-source">&mdash; Helena Brusco, Founder of The Willow Hours</div>
  </blockquote>

  <!-- news -->
  <section class="abs news">
    <div class="abs side-label" style="left:71px;top:125px">BLOG/PODCASTS</div>
    <h2 class="abs display title" style="left:122px;top:62px">Recent News</h2>
    <div class="abs display title" style="left:94px;top:84px">And Podcasts</div>
    <article class="abs post" style="top:137px">
      <div class="thumb" role="img" aria-label="Photo of an open notebook and pen"></div>
      <div class="date">10/10/2022</div><div class="ptitle">Blog Post Title Goes Here</div><div class="more">READ FULL STORY</div>
    </article>
    <article class="abs post" style="top:231px">
      <div class="thumb" role="img" aria-label="Photo of handwritten notes and a pen"></div>
      <div class="date">10/10/2022</div><div class="ptitle">Blog Post Title Goes Here</div><div class="more">READ FULL STORY</div>
    </article>
  </section>

  <!-- footer -->
  <footer>
    <div class="abs footer-col" style="left:38px;top:2770px">services<br>appointment</div>
    <div class="abs footer-col" style="left:135px;top:2770px">info@example.com<br>+1 234 567 890</div>
    <div class="abs footer-col" style="left:252px;top:2770px">terms &amp; conditions<br>privacy policy</div>
    <div class="abs social" style="left:376px;top:2770px"></div>
    <div class="abs social" style="left:405px;top:2770px"></div>
    <div class="abs social" style="left:434px;top:2770px"></div>
    <div class="abs footer-col" style="left:509px;top:2776px;color:#888">&copy; 2022 &middot; The Willow Hours</div>
  </footer>
</main>
</body>
</html>
```